Professional PowerPoint Template for Data Reports, Presentations

We are a small leadership coaching/consulting firm and would like to update our PowerPoint template that we use with our clients, who are typically mid-senior level company professionals. I've attached a sample Powerpoint as well as our branding guide. The cover page is what needs the most work - just doesn't look current/professional enough. We do want to keep the pages after that clean, with come color but enough space for text and graphics.
Target Market(s)
Senior mgmt and HR executives in small-mid sized companies
Font styles to use
Sans Serif
Requirements
Must have
- Professional
- Clean
- Tied to company color scheme/logo
Nice to have
- Our title pages don't usually have many words on them; we'd like a design that has a lot of color - probably still using mainly our blue but accented with other colors.
- Need simple but smart looking pages after cover with lot of space; mostly we have text on the slides. Currently this is often in bullet point style, but we could probably upgrade the options there.
Should not have
- Anything that looks like a marketing style, as we typically use these with our current clients to share results of data collected, project plans, etc.

```html
<!DOCTYPE html>
<html lang="en">
<head>
<meta charset="utf-8">
<title>Keelstone Presentation Template</title>
<link rel="stylesheet" href="https://fonts.googleapis.com/css2?family=Montserrat:wght@700;800&family=Arimo:wght@400;700&display=swap">
<style>
  :root {
    --navy: #415077;
    --orange: #e98153;
    --green: #80b09d;
    --lavender: #dfd9ea;
    --beige: #efebe7;
    --grey: #e6e6e6;
    --tab-blue: #1d4f85;
    --ink: #2b2b33;
    --grid: #d6d3e6;
    --white: #ffffff;
  }
  * { margin: 0; padding: 0; box-sizing: border-box; }
  html, body { width: 1040px; height: 1200px; overflow: hidden; background: var(--white); }
  body { position: relative; font-family: "Arimo", Arial, sans-serif; color: var(--ink); }

  .deck { position: absolute; left: 277px; top: 54px; width: 476px; }
  .slide {
    position: relative; width: 476px; height: 357px; overflow: hidden;
    background: var(--white); border: 1px solid #222;
  }
  .slide + .slide { margin-top: -1px; }

  .slide-title {
    position: absolute; left: 0; width: 476px; text-align: center;
    font-family: "Montserrat", Arial, sans-serif; font-weight: 800;
    font-size: 15px; letter-spacing: 1.6px; color: var(--navy);
  }
  .slide-subtitle {
    position: absolute; left: 0; width: 476px; text-align: center;
    font-size: 12px; color: var(--ink);
  }
  .accent-bar { position: absolute; left: 163px; width: 151px; height: 5px; display: flex; }
  .accent-bar span { height: 100%; }
  .accent-bar .a1 { width: 18px; background: var(--navy); }
  .accent-bar .a2 { width: 25px; background: var(--orange); }
  .accent-bar .a3 { width: 31px; background: var(--green); }
  .accent-bar .a4 { width: 34px; background: var(--lavender); }
  .accent-bar .a5 { width: 43px; background: var(--beige); }

  /* Charts slide */
  .side-strip { position: absolute; left: 281px; top: 0; width: 13px; height: 100%; background: var(--beige); }
  .side-panel { position: absolute; left: 294px; top: 0; right: 0; height: 100%; background: var(--lavender); }
  .chart { position: absolute; left: 0; top: 0; }
  .panel-copy {
    position: absolute; left: 311px; top: 106px; width: 136px;
    font-size: 7.4px; line-height: 9.6px; text-align: justify; color: #3a3a48;
  }
  .point-list { position: absolute; left: 313px; top: 0; list-style: none; }
  .point {
    position: absolute; left: 0; width: 140px; height: 16px;
    display: flex; align-items: center; font-size: 7.4px; color: #3a3a48; white-space: nowrap;
  }
  .point-num {
    width: 16px; height: 16px; margin-right: 8px; flex: none;
    border: 2px solid var(--navy); background: var(--white);
    font-weight: 700; font-size: 8px; color: var(--navy);
    display: flex; align-items: center; justify-content: center;
  }
  .p1 .point-num { box-shadow: -2px -2px 0 var(--orange); }
  .p2 .point-num { box-shadow: -2px -2px 0 var(--green); }
  .p3 .point-num { box-shadow: -2px -2px 0 var(--navy); }
  .p4 .point-num { box-shadow: -2px -2px 0 var(--white); }
  .p5 .point-num { box-shadow: -2px -2px 0 var(--navy); }

  /* Data slide */
  .edge-rule { position: absolute; right: 0; top: 0; width: 3px; height: 100%; background: var(--tab-blue); }
  .brand-tab {
    position: absolute; left: 453px; top: 23px; width: 21px; height: 72px; background: var(--tab-blue);
    display: flex; align-items: center; justify-content: center;
  }
  .brand-tab span {
    transform: rotate(-90deg); white-space: nowrap;
    font-family: "Montserrat", Arial, sans-serif; font-weight: 700;
    font-size: 6.5px; letter-spacing: 1px; color: var(--white);
  }
  .table-frame { position: absolute; left: 73px; top: 134px; width: 318px; height: 95px; background: var(--green); }
  .data-table {
    position: absolute; left: 79px; top: 118px; width: 318px; border-collapse: collapse;
    background: var(--white); font-size: 7.4px; text-align: center;
  }
  .data-table th {
    height: 18px; background: var(--lavender); color: var(--navy); font-weight: 700;
  }
  .data-table td { height: 17.6px; border-bottom: 1px solid #ecebf2; color: #444; }
  .data-table td.emph { color: #111; }
  .data-copy {
    position: absolute; left: 143px; top: 261px; width: 192px;
    font-size: 7.4px; line-height: 9.4px; text-align: center; color: #222;
  }
  .footer-note { position: absolute; left: 0; top: 346px; width: 476px; text-align: center; font-size: 4.6px; color: #333; }

  /* Closing slide */
  .top-band { position: absolute; left: 0; top: 0; width: 100%; height: 14px; background: var(--navy); }
  .closing-bands { position: absolute; left: 0; top: 0; }
  .closing-title {
    position: absolute; left: 0; top: 97px; width: 476px; text-align: center;
    font-family: "Montserrat", Arial, sans-serif; font-weight: 800; font-size: 20px;
    letter-spacing: 1px; color: var(--navy);
  }
  .wordmark {
    position: absolute; left: 0; top: 136px; width: 476px;
    display: flex; align-items: center; justify-content: center; gap: 10px;
    font-family: "Montserrat", Arial, sans-serif; font-weight: 700; font-size: 24px;
    letter-spacing: 2px; color: #1e1e1e;
  }
  .wordmark .dot { width: 26px; height: 26px; border-radius: 50%; background: #1e1e1e; }
</style>
</head>
<body>
<main class="deck">

  <section class="slide charts-slide">
    <div class="side-strip"></div>
    <div class="side-panel"></div>
    <h2 class="slide-title" style="top:26px">CHARTS SLIDE</h2>
    <p class="slide-subtitle" style="top:45px">Lorem ipsum dolor sit amet.</p>
    <div class="accent-bar" style="top:69px"><span class="a1"></span><span class="a2"></span><span class="a3"></span><span class="a4"></span><span class="a5"></span></div>

    <svg class="chart" width="290" height="310" viewBox="0 0 290 310" font-family="Arimo, Arial, sans-serif">
      <g stroke="var(--grid)" stroke-width="0.8">
        <line x1="47" x2="271" y1="112" y2="112"/><line x1="47" x2="271" y1="127.2" y2="127.2"/>
        <line x1="47" x2="271" y1="142.4" y2="142.4"/><line x1="47" x2="271" y1="157.6" y2="157.6"/>
        <line x1="47" x2="271" y1="172.8" y2="172.8"/><line x1="47" x2="271" y1="188" y2="188"/>
        <line x1="47" x2="271" y1="203.2" y2="203.2"/><line x1="47" x2="271" y1="218.4" y2="218.4"/>
        <line x1="47" x2="271" y1="233.6" y2="233.6"/><line x1="47" x2="271" y1="248.8" y2="248.8"/>
        <line x1="47" x2="271" y1="264" y2="264"/>
      </g>
      <g font-size="7.5" fill="#555" text-anchor="end">
        <text x="40" y="115">10</text><text x="40" y="130">9</text><text x="40" y="145">8</text>
        <text x="40" y="160">7</text><text x="40" y="176">6</text><text x="40" y="191">5</text>
        <text x="40" y="206">4</text><text x="40" y="221">3</text><text x="40" y="236">2</text>
        <text x="40" y="252">1</text><text x="40" y="267">0</text>
      </g>
      <g fill="none" stroke-width="2">
        <polyline stroke="var(--orange)" points="63,264 95,233.6 127,233.6 159,188 191,180.4 223,203.2 255,172.8"/>
        <polyline stroke="var(--green)" points="63,248.8 95,218.4 127,195.6 159,172.8 191,188 223,157.6 255,142.4"/>
        <polyline stroke="var(--navy)" points="63,233.6 95,172.8 127,180.4 159,142.4 191,150 223,127.2 255,127.2"/>
      </g>
      <g font-size="7.5" font-weight="700" fill="var(--navy)">
        <rect x="71" y="287" width="11" height="11" fill="var(--orange)"/><text x="87" y="296">Year 1</text>
        <rect x="134" y="287" width="11" height="11" fill="var(--green)"/><text x="150" y="296">Year 2</text>
        <rect x="198" y="287" width="11" height="11" fill="var(--navy)"/><text x="214" y="296">Year 3</text>
      </g>
    </svg>

    <p class="panel-copy">Lorem ipsum dolor sit amet, ut qui tale interesset, pri eu zril solet altera. Quo graeco detracto indoctum ex, vocent oportere usu no, at cetero corpora forensibus per. Eos suas equidem an, per quando nullam rationibus cu.</p>
    <ul class="point-list">
      <li class="point p1" style="top:189px"><span class="point-num">1</span>Lorem ipsum dolor sit amet.</li>
      <li class="point p2" style="top:219px"><span class="point-num">2</span>Lorem ipsum dolor sit amet.</li>
      <li class="point p3" style="top:250px"><span class="point-num">3</span>Lorem ipsum dolor sit amet.</li>
      <li class="point p4" style="top:282px"><span class="point-num">4</span>Lorem ipsum dolor sit amet.</li>
      <li class="point p5" style="top:314px"><span class="point-num">5</span>Lorem ipsum dolor sit amet.</li>
    </ul>
  </section>

  <section class="slide data-slide">
    <div class="edge-rule"></div>
    <div class="brand-tab"><span>KEELSTONE</span></div>
    <h2 class="slide-title" style="top:38px">DATA SLIDE</h2>
    <p class="slide-subtitle" style="top:58px">Lorem ipsum dolor sit amet.</p>
    <div class="accent-bar" style="top:81px"><span class="a1"></span><span class="a2"></span><span class="a3"></span><span class="a4"></span><span class="a5"></span></div>

    <div class="table-frame"></div>
    <table class="data-table">
      <thead><tr><th>Stuff 1</th><th>Stuff 2</th><th>Stuff 3</th><th>Stuff 4</th></tr></thead>
      <tbody>
        <tr><td>Lorem ipsum</td><td class="emph">Ius vivendum</td><td>Eos suas</td><td>Quo graeco</td></tr>
        <tr><td>Dolor sit</td><td>Lorem ipsum</td><td class="emph">Ius vivendum</td><td>Eos suas</td></tr>
        <tr><td>Quo graeco</td><td>Dolor sit</td><td>Lorem ipsum</td><td class="emph">Ius vivendum</td></tr>
        <tr><td>Eos suas</td><td>Quo graeco</td><td>Dolor sit</td><td>Lorem ipsum</td></tr>
        <tr><td class="emph">Ius vivendum</td><td>Eos suas</td><td>Quo graeco</td><td>Dolor sit</td></tr>
      </tbody>
    </table>

    <p class="data-copy">Lorem ipsum dolor sit amet, ut qui tale interesset, pri eu zril solet altera. Quo graeco detracto indoctum ex, vocent oportere usu no, at cetero corpora forensibus per. Eos suas equidem an, per quando nullam rationibus cu.</p>
    <p class="footer-note">© Keelstone Company www.keelstonecompany.com 555-010-0199</p>
  </section>

  <section class="slide closing-slide">
    <div class="top-band"></div>
    <svg class="closing-bands" width="476" height="357" viewBox="0 0 476 357" aria-hidden="true">
      <rect x="0" y="244" width="476" height="113" fill="var(--grey)"/>
      <rect x="0" y="252" width="120" height="6" fill="var(--orange)"/>
      <rect x="120" y="252" width="110" height="6" fill="var(--green)"/>
      <rect x="230" y="252" width="100" height="6" fill="var(--lavender)"/>
      <rect x="0" y="266" width="330" height="91" fill="var(--navy)"/>
    </svg>
    <h2 class="closing-title">THANK YOU</h2>
    <div class="wordmark"><span class="dot"></span>KEELSTONE</div>
  </section>

</main>
</body>
</html>
```